Orthodontic Postcard Design for Mailing to Potential Clients - This is a redesign of an existing one

I need to modify the attached "Back To School" ai file as follows:Front Side:* Back to school - change to - Grand Opening* Excellent orthodontic care... - change to - Excellent orthodontic care for your entire family. Increasing self-esteem by creating beautiful smiles is what we do!* See why so many of your neighbors.. - change to - See why so many of your neighbors are choosing Dr. Pellham for their family orthodontic needs.* Change address to - 2775 Via de la Valle, Suite 101Del Mar, CA 92014(858) 720-1130* Change email address to -www.Braces.CareBack Side:*
Replace "Quality can be fun... with my quote "Classic smiles are what we do!" Dr. Pellham
Map (attached)
Eliminate current pictures - add girl with braces (attached) and my picture (attached)
Back to school... - replaced with a coupon that says Free Initial Orthodontic Consultation - Offer valid for sixty days.* Change address and websiteI would like to do these postcards every six weeks. Do you find the extra large cards more effective than the medium cards? What is the cost difference. I would like to send them to households in the 92014, 92091 and 92067 zip codes.

Target Market(s)

Typically age 7-16, and young adults

Industry/Entity Type

School

Requirements
Must have
• I need this project completed ASAP in order to send it to print.

```html
<!DOCTYPE html>
<html lang="en">
<head>
<meta charset="utf-8">
<title>Pellham Orthodontics – Grand Opening Postcard</title>
<link rel="stylesheet" href="https://fonts.googleapis.com/css2?family=Marcellus&family=Pinyon+Script&family=Sorts+Mill+Goudy&family=Archivo+Black&display=swap">
<style>
  :root {
    --page-bg: #e9e7e4;
    --card-bg: #ffffff;
    --brand-red: #c41e2a;
    --ink: #1d1d1d;
    --marker: #f4f06a;
    --photo-warm: #d9b27a;
    --photo-skin: #e8bfa4;
    --photo-denim: #8fa3b8;
  }
  * { margin: 0; padding: 0; box-sizing: border-box; }
  html, body { width: 1200px; height: 1000px; overflow: hidden; background: var(--page-bg); }
  .postcard {
    position: absolute; left: 60px; top: 230px; width: 1080px; height: 540px;
    background: var(--card-bg); overflow: hidden;
    box-shadow: 0 2px 6px rgba(0,0,0,.18);
    font-family: "Sorts Mill Goudy", Georgia, serif; color: var(--ink);
  }
  .photo { position: absolute; }
  .photo-girl {
    left: 0; top: 0; width: 250px; height: 385px;
    background: linear-gradient(160deg, var(--photo-warm) 0%, var(--photo-skin) 55%, #d98a8a 100%);
  }
  .photo-boy {
    left: 905px; top: 190px; width: 170px; height: 280px; border-radius: 60px 60px 30px 30px;
    background: linear-gradient(180deg, #c9a27a 0%, #c9a27a 12%, var(--photo-denim) 30%, #6f86a0 80%, #e6e6e6 100%);
  }
  .burst { position: absolute; left: 0; top: 0; width: 1080px; height: 540px; }
  .opening-badge {
    position: absolute; left: 937px; top: 2px; width: 143px; height: 88px;
    background: var(--brand-red); border-radius: 8px 0 0 8px;
    color: #fff; text-align: center; padding-top: 6px;
  }
  .opening-badge .title { font-family: "Archivo Black", Arial, sans-serif; font-size: 22px; line-height: 24px; }
  .opening-badge .sub { font-size: 15px; line-height: 15px; margin-top: 2px; }
  .headline-group { font-weight: normal; }
  .headline { font-family: "Marcellus", "Optima", serif; position: absolute; color: var(--ink); white-space: nowrap; font-weight: normal; line-height: 1.1; }
  .headline-brace { left: 558px; top: 2px; font-size: 72px; }
  .headline-yourself { left: 452px; top: 66px; font-size: 68px; }
  .headline-yourself small { font-size: 50px; }
  .headline-classic {
    position: absolute; left: 258px; top: 92px; font-family: "Pinyon Script", cursive;
    font-size: 164px; color: var(--brand-red); white-space: nowrap; line-height: 1; font-weight: normal;
  }
  .headline-smile { left: 660px; top: 140px; font-size: 86px; }
  .intro {
    position: absolute; left: 330px; top: 242px; width: 560px; text-align: center;
    font-size: 22px; line-height: 26px;
  }
  .accent-band {
    position: absolute; left: 445px; top: 342px; width: 635px; height: 48px;
    background: linear-gradient(90deg, #fbe9e9 0%, #e27a7a 25%, var(--brand-red) 55%, var(--brand-red) 100%);
  }
  .neighbors {
    position: absolute; left: 400px; top: 406px; width: 520px; text-align: center;
    font-size: 20px; line-height: 26px; white-space: nowrap;
  }
  .neighbors span { background: linear-gradient(transparent 45%, var(--marker) 45%, var(--marker) 85%, transparent 85%); padding: 0 4px; }
  .brand-name {
    position: absolute; left: 20px; top: 378px; width: 380px;
    color: var(--brand-red); font-size: 64px; line-height: 64px; text-align: center;
  }
  .brand-name .line2 { display: block; font-size: 38px; line-height: 46px; }
  .address { position: absolute; left: 422px; top: 470px; font-size: 14px; line-height: 19px; font-style: normal; }
  .address .city { padding-left: 32px; }
  .address .phone { padding-left: 40px; font-size: 17px; }
  .web { position: absolute; left: 780px; top: 476px; width: 220px; text-align: center; color: var(--brand-red); }
  .web .lead { font-size: 21px; line-height: 24px; }
  .web .url { font-size: 24px; line-height: 28px; }
</style>
</head>
<body>
<main class="postcard">
  <div class="photo photo-girl" role="img" aria-label="Smiling teenage girl with long blonde hair wearing braces"></div>

  <svg class="burst" viewBox="0 0 1080 540" aria-hidden="true">
    <polygon fill="#c41e2a" points="1180,60 1084,70 1174,104 1079,89 1157,145 1069,106 1130,180 1056,119 1095,207 1039,129 1054,224 1020,134 1010,230 1000,134 966,224 981,129 925,207 964,119 890,180 951,106 863,145 941,89 846,104 936,70 840,60 936,50 846,16 941,31 863,-25 951,14 890,-60 964,1 925,-87 981,-9 966,-104 1000,-14 1010,-110 1020,-14 1054,-104 1039,-9 1095,-87 1056,1 1130,-60 1069,14 1157,-25 1079,31 1174,16 1084,50"/>
  </svg>
  <div class="opening-badge">
    <div class="title">GRAND<br>OPENING!</div>
    <div class="sub">Now accepting<br>new patients.</div>
  </div>

  <h1 class="headline-group">
    <span class="headline headline-brace">Brace</span>
    <span class="headline headline-yourself">Yourself <small>for a</small></span>
    <span class="headline-classic">Classic</span>
    <span class="headline headline-smile">Smile!</span>
  </h1>

  <p class="intro">Excellent orthodontic care for your entire family.<br>Increasing self-esteem by creating<br>beautiful smiles is what we do!</p>

  <div class="accent-band"></div>
  <div class="photo photo-boy" role="img" aria-label="Teenage boy with curly hair sitting and hugging his knees"></div>

  <p class="neighbors"><span>See why so many of your neighbors are choosing</span><br><span>Dr. Pellham for their family orthodontic needs.</span></p>

  <div class="brand-name">Pellham<span class="line2">Orthodontics</span></div>

  <address class="address">
    4318 Camino Rosario • Suite 204<br>
    <span class="city">Del Mar, CA 92014</span><br>
    <span class="phone">(858) 555-0147</span>
  </address>

  <div class="web">
    <div class="lead">visit us at</div>
    <div class="url">www.Grinwell.Care</div>
  </div>
</main>
</body>
</html>
```